Real Estate Entrepreneur needs a business card

I am a real estate entrepreneur, I buy houses for investment purposes, I act as a real estate agent representing buyers and sellers in residential home transactions, I am a contractor that does a wide range of home repairs and construction. I'd like a design that can stick with me through the years as my business grows and morphs to fit any niche I decide to pursue as markets change.

Target Market(s)

Anyone with interest that may be related to real estate.

Industry/Entity Type

Real Estate

Contact Information for Business Card

A card that stands out and doesn't put me in any one box. My business will evolve over time and I need a card that can stay relevant.

Colors

Designer to choose colors to be used in the design.

Requirements
Must have
• Character
Nice to have
• I'm open
Should not have
• Cliche houses and hammers

```html
<!DOCTYPE html>
<html lang="en">
<head>
<meta charset="UTF-8">
<title>Rhett Calder — Business Card</title>
<link href="https://fonts.googleapis.com/css2?family=Work+Sans:wght@400;500;700&display=swap" rel="stylesheet">
<style>
  :root {
    --backdrop: #161616;
    --card: #1f1f1f;
    --card-edge: #2a2a2a;
    --ink: #f4f4f4;
    --ink-soft: #dcdcdc;
    --rule: #cfcfcf;
  }
  * { margin: 0; padding: 0; box-sizing: border-box; }
  html, body {
    width: 1200px;
    height: 900px;
    overflow: hidden;
    background: var(--backdrop);
    font-family: "Work Sans", Arial, sans-serif;
  }
  .canvas {
    width: 1200px;
    height: 900px;
    display: flex;
    flex-direction: column;
    align-items: center;
    justify-content: center;
    gap: 40px;
    background: radial-gradient(ellipse at 50% 40%, #262626 0%, var(--backdrop) 70%);
  }
  .card {
    position: relative;
    width: 630px;
    height: 360px;
    background: linear-gradient(135deg, var(--card) 0%, #232323 60%, #2b2b2b 100%);
    border: 1px solid var(--card-edge);
    box-shadow: 0 18px 40px rgba(0, 0, 0, 0.55);
    color: var(--ink);
  }
  .card-front {
    display: flex;
    align-items: center;
    justify-content: center;
  }
  .brand-name {
    font-weight: 700;
    font-size: 50px;
    letter-spacing: 5px;
    text-transform: uppercase;
    color: var(--ink);
  }
  .divider {
    position: absolute;
    left: 52px;
    right: 52px;
    top: 196px;
    height: 1px;
    background: var(--rule);
  }
  .person {
    position: absolute;
    right: 52px;
    top: 128px;
    text-align: right;
  }
  .person-name {
    font-weight: 500;
    font-size: 29px;
    letter-spacing: 3px;
    text-transform: uppercase;
  }
  .person-role {
    font-size: 16px;
    letter-spacing: 1.5px;
    color: var(--ink-soft);
  }
  .contact {
    position: absolute;
    left: 52px;
    top: 222px;
    display: grid;
    grid-template-columns: 68px 18px auto;
    row-gap: 8px;
    font-size: 17px;
    letter-spacing: 1.5px;
    color: var(--ink-soft);
  }
</style>
</head>
<body>
  <main class="canvas">
    <section class="card card-front">
      <div class="brand-name">Rhett Calder</div>
    </section>

    <section class="card card-back">
      <div class="person">
        <div class="person-name">Rhett Calder</div>
        <div class="person-role">Director</div>
      </div>
      <div class="divider"></div>
      <div class="contact">
        <span>Phone</span><span>:</span><span>(03) 5550 4182</span>
        <span>Email</span><span>:</span><span>info@rhettcalder.com</span>
        <span>Web</span><span>:</span><span>www.rhettcalder.com</span>
      </div>
    </section>
  </main>
</body>
</html>
```